RTV Electrical – Fridge Magnet & Letterbox Leaflet

Overview
We are a local electrical contractor based in Gooseberry Hill in the Perth Hills (Western Australia).
We are looking for a designer to create:
1️⃣ A fridge magnet design
2️⃣ A matching letterbox leaflet (A6 or DL)
The goal is to create clean, professional marketing that feels local and trustworthy, not flashy advertising.
The designs must feel like a high-quality local trades business, appealing to homeowners in suburbs such as:
Kalamunda
Gooseberry Hill
Lesmurdie
Walliston
Pickering Brook
Design Style
The design should feel:
✔ Local
✔ Authentic
✔ Professional
✔ Trustworthy
✔ Clean and simple
NOT:
✖ Cheap advertising
✖ Overly flashy
✖ Busy or cluttered
Think premium local tradesman, not mass marketing.
Branding
Use our brand colours inspired by our van:
Primary colours
Navy Blue
White
Accent colour
Yellow / gold highlight
Design should match the look of our work van branding.
Images Provided
We will provide:
✔ Company logo
✔ Photo of our branded van in the Perth Hills
The van photo should be used in the leaflet design to reinforce our local presence.
Fridge Magnet Design
Size suggestion:
90mm x 55mm
Purpose:
Homeowners keep this magnet so they can easily call a trusted electrician.
Must include:
RTV Electrical Contracting
Local Perth Hills Electrician
Based in Gooseberry Hill
Phone number (large and clear)
📞 0491 726 054
Services:
• Fault finding
• Switchboard upgrades
• Lighting & power
• Ceiling fans
• Smoke alarm compliance
Also include:
⭐ 110+ Starfold Reviews
Website:
www.rtvelectrical.com.au
Design should be very simple and easy to read from across a kitchen.
Leaflet Design
Size options:
A6 or DL
Purpose:
Letterbox drop marketing in Perth Hills suburbs.
Front Side
Headline:
WE'RE WORKING IN YOUR AREA
Subtext:
Local electrician based in Gooseberry Hill
Include:
✔ Photo of our van
✔ RTV logo
✔ Key services
Services:
• Fault finding
• Switchboard upgrades
• Lighting & power
• Ceiling fans
• Smoke alarm compliance
Call to action:
📞 Call Marcus – 0491 726 054
⭐ 110+ Five-Star Starfold Reviews
Back Side
Headline:
Your Local Perth Hills Electrician
Servicing:
Kalamunda
Gooseberry Hill
Lesmurdie
Walliston
Pickering Brook
Short message:
Reliable electrical work across the Perth Hills.
Call Marcus
📞 0491 726 054
Website:
www.rtvelectrical.com.au
EC47286
Target Audience
Homeowners in the Perth Hills aged 35–70.
Many homes are older properties and often need electrical upgrades, repairs and safety work.
Design should appeal to homeowners who value reliability and local service.
Deliverables
Designers must provide:
✔ Print-ready files
✔ Editable source files
✔ High resolution files
For:
Fridge magnet
Leaflet front and back
Final Notes
This design should communicate:
✔ Trusted local electrician
✔ Established business
✔ Professional service
✔ Easy to contact
The goal is to create marketing people will keep, not throw away.

```html
<!DOCTYPE html>
<html lang="en">
<head>
<meta charset="utf-8">
<title>RTV Electrical – Leaflet & Magnet</title>
<link rel="stylesheet" href="https://fonts.googleapis.com/css2?family=Poppins:wght@500;600;700;800&family=Roboto:wght@400;500;700;900&display=swap">
<style>
:root{
  --navy:#12295a;
  --navy-deep:#0b1d44;
  --gold:#f3b61f;
  --gold-soft:#f8c63a;
  --white:#ffffff;
  --ink:#1b2233;
  --red:#d7262a;
  --stage:#999a9c;
}
*{box-sizing:border-box;margin:0;padding:0}
html,body{width:1119px;height:1200px;overflow:hidden;background:var(--stage)}
body{position:relative;font-family:"Roboto",Arial,sans-serif;color:var(--ink)}
.piece{position:absolute;background:var(--white);overflow:hidden;box-shadow:0 2px 6px rgba(0,0,0,.35)}
.leaflet-front{left:62px;top:45px;width:478px;height:681px}
.leaflet-back{left:589px;top:45px;width:475px;height:681px}
.magnet{left:199px;top:767px;width:618px;height:377px;background:var(--navy)}
.abs{position:absolute}
.center{left:0;right:0;text-align:center}

/* photo placeholders */
.photo-van{left:0;top:0;width:100%;height:262px;background:linear-gradient(180deg,#9cc3e6 0%,#cfdde6 28%,#4a5f86 48%,#1c2c55 66%,#2b2f38 82%,#4a3f30 100%)}
.photo-board{left:0;top:0;width:100%;height:240px;background:linear-gradient(135deg,#8a6b4c 0%,#b58a5a 30%,#c9c7c2 55%,#e4e2de 75%,#8d8f92 100%)}
.wedges{left:0;top:150px;width:100%;height:170px}

.headline{font-family:"Poppins",Arial,sans-serif;font-weight:700;line-height:1.12}
.gold{color:var(--gold)}
.navy{color:var(--navy)}

.brand{display:flex;align-items:center;gap:7px;font-family:"Roboto",Arial,sans-serif;font-weight:500;color:var(--navy);font-size:15px;line-height:1.1}
.brand .mark{width:26px;height:40px;background:var(--navy);border-radius:3px}

.tagline{font-family:"Poppins",Arial,sans-serif;font-weight:700;font-size:17px;color:var(--white);text-align:center;line-height:1.15;text-shadow:0 1px 3px rgba(0,0,0,.6)}

.review-badge{left:333px;top:165px;width:118px;height:118px;border-radius:50%;background:var(--red);border:4px solid var(--white);color:var(--white);text-align:center;font-family:"Roboto",Arial,sans-serif;display:flex;flex-direction:column;align-items:center;justify-content:center;gap:2px}
.review-badge .name{font-weight:700;font-size:16px}
.review-badge .stars{color:var(--gold);font-size:11px;letter-spacing:1px}
.review-badge .count{font-weight:900;font-size:9.5px;line-height:1.15}

.intro{font-size:13px;color:var(--ink)}
.locate{display:flex;align-items:center;justify-content:center;gap:8px;font-weight:500;font-size:15px;line-height:1.2;color:var(--ink)}
.pill{background:var(--gold);color:var(--navy);font-weight:700;border-radius:14px;text-align:center;font-family:"Roboto",Arial,sans-serif}

.services{left:20px;right:20px;display:flex}
.service{flex:1;display:flex;flex-direction:column;align-items:center;gap:6px;border-left:1px solid #c9ccd3;font-weight:500;font-size:12.5px;text-align:center;line-height:1.15;color:var(--ink)}
.service:first-child{border-left:none}
.icon{width:52px;height:52px;border-radius:50%;display:flex;align-items:center;justify-content:center;border:3px solid var(--gold)}
.icon.navy-bg{background:var(--navy)}
.icon.gold-bg{background:var(--gold);border-color:var(--navy)}
.icon svg{width:28px;height:28px}

.footer{left:0;bottom:0;width:100%;height:73px;background:var(--navy)}
.footer .call{left:22px;top:10px;display:flex;align-items:center;gap:6px}
.footer .call-label{color:var(--gold);font-weight:700;font-size:12.5px}
.footer .phone-dot{width:22px;height:22px;border-radius:50%;background:var(--gold);display:flex;align-items:center;justify-content:center}
.footer .number{color:var(--white);font-family:"Roboto",Arial,sans-serif;font-weight:700;font-size:33px;letter-spacing:.3px}
.footer .meta{left:22px;top:48px;display:flex;align-items:center;gap:10px;color:var(--white);font-weight:500;font-size:15px}
.footer .lic{display:flex;align-items:center;gap:6px;padding-right:10px;border-right:1px solid rgba(255,255,255,.6)}
.follow{right:0;top:0;width:70px;height:100%;background:var(--gold);clip-path:polygon(0 0,100% 0,100% 100%,0 100%,24% 50%);display:flex;flex-direction:column;align-items:center;justify-content:center;padding-left:14px;color:var(--navy);font-weight:700;font-size:11px;line-height:1.1;text-align:center}
.follow .sq{width:11px;height:11px;background:var(--navy);margin-bottom:3px}

.callout{left:16px;top:164px;width:118px;height:118px;border-radius:50%;background:var(--red);border:3px dashed var(--white);outline:3px solid var(--red);color:var(--white);display:flex;flex-direction:column;align-items:center;justify-content:center;text-align:center;font-size:10.5px;line-height:1.25;padding:10px 12px}
.callout b{font-size:11.5px;font-weight:700;margin-bottom:4px;line-height:1.2}

.rule-title{left:20px;right:20px;top:380px;display:flex;align-items:center;gap:8px;font-family:"Poppins",Arial,sans-serif;font-weight:600;font-size:19px;color:var(--ink);line-height:1.1;text-align:center}
.rule-title .line{flex:1;height:1px;background:var(--ink)}

.suburbs{left:16px;right:16px;top:448px;display:flex}
.suburb{flex:1;display:flex;flex-direction:column;align-items:center;gap:8px;border-left:1px solid #c9ccd3;font-weight:700;font-size:12px;text-align:center;line-height:1.2;color:var(--ink);padding-bottom:4px}
.suburb:first-child{border-left:none}
.suburb svg{width:32px;height:38px}

.magnet-top{left:0;top:0;width:100%;height:200px}
.m-icons{left:45px;right:45px;top:112px;display:flex;justify-content:space-between}
.m-icon{display:flex;align-items:center;gap:6px;font-weight:700;font-size:11.5px;line-height:1.05;color:var(--navy)}
.m-icon .dot{width:30px;height:30px;border-radius:50%;background:var(--navy);border:2px solid var(--white);display:flex;align-items:center;justify-content:center}
.m-icon .dot svg{width:17px;height:17px}
.m-phone{left:26px;top:166px;width:330px;height:44px;background:var(--white);border-radius:22px;display:flex;align-items:center;gap:8px;padding-left:8px;font-weight:700;font-size:36px;color:var(--navy-deep)}
.m-phone .phone-dot{width:28px;height:28px;border-radius:50%;border:2px solid var(--navy);display:flex;align-items:center;justify-content:center}
.m-van{left:265px;top:170px;width:338px;height:170px;border-radius:14px 40px 10px 10px;background:linear-gradient(170deg,#3b4f7d 0%,#1a2b57 45%,#0e1c3f 80%,#2a2f3a 100%)}
.m-reviews{left:30px;top:232px;color:var(--white);text-align:center}
.m-reviews .big{font-weight:900;font-size:30px;color:var(--gold);line-height:1}
.m-reviews .small{font-weight:700;font-size:9px;line-height:1.15}
.m-rating{left:128px;top:238px;text-align:center}
.m-rating .name{font-family:"Roboto",Arial,sans-serif;font-weight:500;font-size:28px;color:var(--white);line-height:1}
.m-rating .stars{color:var(--gold);font-size:14px;letter-spacing:2px}
.m-brand{left:26px;top:305px;color:var(--white);display:flex;align-items:center;gap:7px;font-weight:500;font-size:16px;line-height:1.1}
.m-brand .mark{width:24px;height:40px;border-radius:3px;background:var(--white)}
.m-email{left:180px;top:312px;color:var(--white);font-weight:700;font-size:19px}
</style>
</head>
<body>

<svg width="0" height="0" style="position:absolute" aria-hidden="true">
  <defs>
    <symbol id="i-phone" viewBox="0 0 24 24"><path d="M6.6 10.8a15 15 0 0 0 6.6 6.6l2.2-2.2c.3-.3.7-.4 1-.2 1.1.4 2.3.6 3.6.6.6 0 1 .4 1 1V20c0 .6-.4 1-1 1A17 17 0 0 1 3 4c0-.6.4-1 1-1h3.5c.6 0 1 .4 1 1 0 1.3.2 2.5.6 3.6.1.3 0 .7-.2 1z"/></symbol>
    <symbol id="i-pin" viewBox="0 0 24 30"><path d="M12 0C5.4 0 0 5.2 0 11.6 0 20 12 30 12 30s12-10 12-18.4C24 5.2 18.6 0 12 0zm0 16.5a5 5 0 1 1 0-10 5 5 0 0 1 0 10z"/></symbol>
    <symbol id="i-search" viewBox="0 0 24 24"><rect x="3" y="2" width="12" height="16" rx="1.5" fill="none" stroke="currentColor" stroke-width="2"/><circle cx="14" cy="13" r="4.5" fill="none" stroke="currentColor" stroke-width="2.2"/><path d="M17.5 16.5L22 21" stroke="currentColor" stroke-width="2.6" stroke-linecap="round"/></symbol>
    <symbol id="i-board" viewBox="0 0 24 24"><rect x="3" y="5" width="18" height="12" rx="2" fill="none" stroke="currentColor" stroke-width="2"/><circle cx="9" cy="11" r="2.5" fill="none" stroke="currentColor" stroke-width="1.8"/><circle cx="15" cy="11" r="2.5" fill="none" stroke="currentColor" stroke-width="1.8"/><path d="M7 17v3M17 17v3" stroke="currentColor" stroke-width="2"/></symbol>
    <symbol id="i-bulb" viewBox="0 0 24 24"><path d="M12 3a6 6 0 0 0-3.5 10.9V16h7v-2.1A6 6 0 0 0 12 3z" fill="currentColor"/><rect x="9" y="17" width="6" height="2" fill="currentColor"/><rect x="10" y="20" width="4" height="1.6" fill="currentColor"/></symbol>
    <symbol id="i-fan" viewBox="0 0 24 24"><path d="M12 2v6" stroke="currentColor" stroke-width="2"/><circle cx="12" cy="10" r="2.2" fill="currentColor"/><path d="M12 10L4 21M12 10l8 11M12 10v12" stroke="currentColor" stroke-width="2" stroke-linecap="round"/></symbol>
    <symbol id="i-alarm" viewBox="0 0 24 24"><rect x="3" y="4" width="18" height="4" rx="1" fill="currentColor"/><path d="M5 9h14l-2 5H7z" fill="currentColor"/><path d="M8 16v2M12 16v3M16 16v2" stroke="currentColor" stroke-width="1.8" stroke-linecap="round"/></symbol>
    <symbol id="i-card" viewBox="0 0 24 16"><rect x="1" y="1" width="22" height="14" rx="2" fill="none" stroke="currentColor" stroke-width="2"/><rect x="4" y="4" width="6" height="6" fill="currentColor"/><path d="M13 5h7M13 9h7M4 12h16" stroke="currentColor" stroke-width="1.6"/></symbol>
  </defs>
</svg>

<!-- Leaflet front -->
<section class="piece leaflet-front">
  <div class="abs photo-van" role="img" aria-label="Photo of the navy RTV Electrical branded work van parked in the bushland of the Perth Hills"></div>
  <svg class="abs wedges" viewBox="0 0 478 170" preserveAspectRatio="none">
    <polygon points="0,45 239,105 0,150" fill="var(--navy)"/>
    <polygon points="478,45 239,105 478,150" fill="var(--navy)"/>
    <polygon points="0,150 239,105 478,150 478,170 0,170" fill="#ffffff"/>
  </svg>
  <p class="abs tagline center" style="top:198px">Need anything while<br><span class="gold">we're in the area?</span></p>
  <div class="abs review-badge">
    <span class="name">Starfold</span>
    <span class="stars">★★★★★</span>
    <span class="count">110+ LOCAL 5-STAR<br>STARFOLD REVIEWS</span>
  </div>

  <div class="abs brand" style="left:170px;top:274px"><span class="mark"></span><span>RTV Electrical<br>Contracting</span></div>

  <h1 class="abs headline center gold" style="top:326px;font-size:34px">Working For Your</h1>
  <h2 class="abs headline center navy" style="top:364px;font-size:34px">Neighbour Today</h2>
  <p class="abs intro center" style="top:408px">Hi neighbour – we're currently carrying out electrical work nearby</p>
  <div class="abs locate center" style="top:428px">
    <svg width="20" height="26" style="color:var(--red);fill:currentColor"><use href="#i-pin"/></svg>
    <span style="text-align:left">Local Perth Hills electrician<br>in Gooseberry Hill</span>
  </div>
  <div class="abs pill" style="left:89px;top:472px;width:300px;height:27px;line-height:27px;font-size:14.5px">Common Electrical Jobs We Help With</div>

  <div class="abs services" style="top:508px">
    <div class="service"><span class="icon navy-bg"><svg style="color:var(--gold)"><use href="#i-search"/></svg></span>Fault<br>finding</div>
    <div class="service"><span class="icon gold-bg"><svg style="color:var(--navy)"><use href="#i-board"/></svg></span>Switchboard<br>upgrades</div>
    <div class="service"><span class="icon navy-bg"><svg style="color:var(--gold)"><use href="#i-bulb"/></svg></span>Lighting<br>&amp; power</div>
    <div class="service"><span class="icon gold-bg"><svg style="color:var(--navy)"><use href="#i-fan"/></svg></span>Ceiling<br>fans</div>
    <div class="service"><span class="icon navy-bg"><svg style="color:var(--gold)"><use href="#i-alarm"/></svg></span>Smoke alarm<br>compliance</div>
  </div>

  <footer class="abs footer">
    <div class="abs call"><span class="call-label">Call Marcus</span><span class="phone-dot"><svg width="13" height="13" style="fill:var(--navy)"><use href="#i-phone"/></svg></span><span class="number">0491 726 054</span></div>
    <div class="abs meta"><span class="lic"><svg width="18" height="12" style="color:var(--gold)"><use href="#i-card"/></svg>EC47286</span><span>admin@rtvelectrical.com.au</span></div>
    <div class="abs follow"><span class="sq"></span>Follow<br>us on</div>
  </footer>
</section>

<!-- Leaflet back -->
<section class="piece leaflet-back">
  <div class="abs photo-board" role="img" aria-label="Photo of an older switchboard with a worn copper busbar and hidden wiring fault"></div>
  <svg class="abs wedges" viewBox="0 0 475 170" preserveAspectRatio="none" style="top:140px">
    <polygon points="0,92 475,92 475,170 0,170" fill="#ffffff"/>
    <polygon points="0,60 190,92 0,150" fill="var(--navy)"/>
    <polygon points="475,30 310,95 475,150" fill="var(--navy)"/>
  </svg>
  <div class="abs callout"><b>Looks OK at<br>first glance...</b>Hidden faults like this can be dangerous.</div>
  <div class="abs brand" style="left:172px;top:232px"><span class="mark"></span><span>RTV Electrical<br>Contracting</span></div>

  <h1 class="abs headline center" style="top:285px;font-size:36px"><span class="gold">Your</span> <span class="navy">Local Perth</span></h1>
  <h2 class="abs headline center" style="top:333px;font-size:36px"><span class="navy">Hills</span> <span class="gold">Electrician</span></h2>

  <div class="abs rule-title"><span class="line"></span><span>Working Across<br>the Perth Hills</span><span class="line"></span></div>

  <div class="abs suburbs">
    <div class="suburb"><svg style="fill:var(--navy)"><use href="#i-pin"/></svg>Kalamunda<br>&nbsp;</div>
    <div class="suburb"><svg style="fill:var(--gold)"><use href="#i-pin"/></svg>Gooseberry<br>Hill</div>
    <div class="suburb"><svg style="fill:var(--navy)"><use href="#i-pin"/></svg>Lesmurdie<br>&nbsp;</div>
    <div class="suburb"><svg style="fill:var(--gold)"><use href="#i-pin"/></svg>Walliston<br>&nbsp;</div>
    <div class="suburb"><svg style="fill:var(--navy)"><use href="#i-pin"/></svg>Pickering<br>Brook</div>
  </div>

  <div class="abs pill" style="left:27px;top:552px;width:421px;height:36px;line-height:32px;font-size:13.5px;border:2px solid var(--navy);border-radius:10px;color:var(--navy-deep)">Reliable electrical work across <svg width="11" height="14" style="fill:var(--red);vertical-align:-2px"><use href="#i-pin"/></svg> Perth Hills and Beyond!!</div>

  <footer class="abs footer">
    <div class="abs call"><span class="call-label">Call Marcus</span><span class="phone-dot"><svg width="13" height="13" style="fill:var(--navy)"><use href="#i-phone"/></svg></span><span class="number">0491 726 054</span></div>
    <div class="abs meta"><span class="lic"><svg width="18" height="12" style="color:var(--gold)"><use href="#i-card"/></svg>EC47286</span><span>admin@rtvelectrical.com.au</span></div>
    <div class="abs follow"><span class="sq"></span>Follow<br>us on</div>
  </footer>
</section>

<!-- Fridge magnet -->
<section class="piece magnet">
  <svg class="abs magnet-top" viewBox="0 0 618 200" preserveAspectRatio="none">
    <path d="M0 0H618V150Q420 138 300 170T0 188Z" fill="var(--gold)"/>
  </svg>
  <h1 class="abs headline center navy" style="top:22px;font-size:30px">Your Local Perth Hills Electrician</h1>
  <div class="abs locate center" style="top:70px;font-size:21px;font-weight:400;color:var(--navy-deep)">
    <svg width="18" height="23" style="fill:var(--red)"><use href="#i-pin"/></svg>Gooseberry Hill
  </div>
  <div class="abs m-icons">
    <div class="m-icon"><span class="dot"><svg style="color:var(--gold)"><use href="#i-search"/></svg></span>Fault<br>finding</div>
    <div class="m-icon"><span class="dot"><svg style="color:var(--gold)"><use href="#i-board"/></svg></span>Switchboard<br>upgrades</div>
    <div class="m-icon"><span class="dot"><svg style="color:var(--gold)"><use href="#i-bulb"/></svg></span>Lighting<br>&amp; power</div>
    <div class="m-icon"><span class="dot"><svg style="color:var(--gold)"><use href="#i-alarm"/></svg></span>Smoke alarm<br>compliance</div>
    <div class="m-icon"><span class="dot"><svg style="color:var(--gold)"><use href="#i-fan"/></svg></span>Ceiling<br>fans</div>
  </div>
  <div class="abs m-van" role="img" aria-label="Photo of the navy RTV Electrical branded work van"></div>
  <div class="abs m-phone"><span class="phone-dot"><svg width="15" height="15" style="fill:var(--navy)"><use href="#i-phone"/></svg></span>0491 726 054</div>
  <div class="abs m-reviews"><div class="big">110+</div><div class="small">LOCAL 5-STAR<br>STARFOLD REVIEWS</div></div>
  <div class="abs m-rating"><div class="name">Starfold</div><div class="stars">★★★★★</div></div>
  <div class="abs m-brand"><span class="mark"></span><span>RTV Electrical<br>Contracting</span></div>
  <div class="abs m-email">admin@rtvelectrical.com.au</div>
</section>

</body>
</html>
```